Whole Body Cryotherapy Business needs a Brochure

We need a brochure for marketing events of our spa. The name of the business is FrostHaven. Our website is www.frosthavenspa-example.com. We are located in New York City at the Lindenmark. We need an eye catching brochure that discusses the health benefits of whole body cryotherapy. We need an editable file to be able to tweak the language of the brochure. The contact information that should be on the brochure is as follows:

FrostHaven
Lindenmark, 482 W. 19th Street
New York, NY 10388

Phone: (855) 614-3098

EMail: frosthavenspa@mailbox-example.com

We prefer a color scheme that mainly uses blue, but are open to any design that is eye catching.

We need the brochure to fit on 8.5" x 11" paper.

Requirements
Must have
• Must have space for the following paragraphs (use Lorem Ipsem and we can fill in later): (1) What is Whole Body Cryotherapy and (2) What makes FrostHaven different.

```html
<!DOCTYPE html>
<html lang="en">
<head>
<meta charset="utf-8">
<title>FrostHaven Trifold Brochure</title>
<link rel="stylesheet" href="https://fonts.googleapis.com/css2?family=Lato:wght@400;700&family=Montserrat:wght@500;600;700&family=Oswald:wght@300&family=Questrial&display=swap">
<style>
  :root {
    --page-bg: #e9ebef;
    --paper: #ffffff;
    --ink: #1d1f24;
    --ink-soft: #3b3f47;
    --brand-blue: #2f8af0;
    --deep-blue: #0f58c9;
    --deep-blue-dark: #0a47a8;
    --periwinkle: #6b7ff0;
    --dark-panel: #141517;
    --dark-panel-light: #4a4c50;
    --footer-grey: #eeeff1;
    --white: #ffffff;
  }
  * { box-sizing: border-box; margin: 0; padding: 0; }
  html, body { width: 1200px; height: 902px; overflow: hidden; }
  body { background: var(--page-bg); font-family: "Lato", sans-serif; }

  .brochure {
    position: absolute; left: 50px; top: 60px;
    width: 1100px; height: 783px;
    background: var(--paper);
    box-shadow: 0 6px 22px rgba(0,0,0,0.18);
    overflow: hidden;
  }
  .artwork { position: absolute; inset: 0; }

  .block { position: absolute; }

  /* left panel */
  .section-title {
    font-family: "Montserrat", sans-serif; font-weight: 700;
    font-size: 15px; color: var(--ink);
  }
  .section-title--light { color: var(--white); }
  .body-copy {
    font-size: 11.4px; line-height: 14.6px; color: var(--ink-soft);
    text-align: justify;
  }
  .body-copy--light { color: var(--white); }
  .body-copy + .body-copy { margin-top: 9px; }
  .intro { left: 32px; top: 31px; width: 324px; }
  .intro .section-title { margin-bottom: 8px; }
  .benefit-list { left: 112px; top: 156px; width: 240px; list-style: none; }
  .benefit-list li {
    position: relative; padding-left: 24px;
    font-size: 11.4px; line-height: 14.6px; color: var(--ink-soft);
    margin-bottom: 6px;
  }
  .benefit-list li::before {
    content: ""; position: absolute; left: 0; top: 3px;
    width: 9px; height: 9px; border-radius: 50%; background: var(--brand-blue);
  }
  .difference { left: 28px; top: 500px; width: 328px; }
  .difference .section-title { margin-bottom: 16px; }

  /* middle panel */
  .contact { left: 381px; top: 0; width: 354px; text-align: center; }
  .brand-mark {
    display: block; width: 52px; height: 52px; margin: 49px auto 0;
    border: 3px solid var(--brand-blue); border-radius: 50%;
  }
  .brand-name {
    font-family: "Montserrat", sans-serif; font-weight: 600;
    font-size: 25px; color: var(--brand-blue); margin-top: 10px;
  }
  .address {
    font-family: "Montserrat", sans-serif; font-weight: 500;
    font-size: 15.5px; line-height: 20px; color: var(--ink);
    margin-top: 62px; font-style: normal;
  }
  .contact-line {
    display: flex; align-items: center; justify-content: center; gap: 7px;
    font-family: "Montserrat", sans-serif; font-weight: 500;
    font-size: 15px; color: var(--ink); margin-top: 6px;
  }
  .contact-line--small { font-size: 13.2px; }
  .contact-line svg { width: 13px; height: 13px; flex: none; }

  /* right panel */
  .cover { left: 735px; top: 0; width: 365px; height: 783px; text-align: center; }
  .cover-mark {
    position: absolute; left: 150px; top: 338px;
    width: 70px; height: 70px; border: 3px solid var(--white); border-radius: 50%;
  }
  .cover-name {
    position: absolute; left: 0; right: 0; top: 420px;
    font-family: "Montserrat", sans-serif; font-weight: 600;
    font-size: 34px; color: var(--white);
  }
  .headline-top {
    position: absolute; left: 0; right: 0; top: 488px;
    font-family: "Oswald", sans-serif; font-weight: 300;
    font-size: 36px; letter-spacing: 0.5px; color: var(--brand-blue);
  }
  .headline-main {
    position: absolute; left: 0; right: 0; top: 516px;
    font-family: "Oswald", sans-serif; font-weight: 300;
    font-size: 82px; line-height: 100px; color: var(--white);
  }
  .tagline {
    position: absolute; left: 0; right: 0; top: 630px;
    font-family: "Questrial", sans-serif; font-size: 22px; line-height: 29px;
    color: var(--brand-blue);
  }
  .cover-url {
    position: absolute; left: 0; right: 0; top: 736px;
    font-family: "Montserrat", sans-serif; font-weight: 500;
    font-size: 13px; letter-spacing: 2px; color: var(--brand-blue);
  }
</style>
</head>
<body>
<main class="brochure">
  <svg class="artwork" width="1100" height="783" viewBox="0 0 1100 783">
    <defs>
      <linearGradient id="blueFill" x1="0" y1="0" x2="0" y2="1">
        <stop offset="0" stop-color="#1a6be0"/>
        <stop offset="1" stop-color="#0a47a8"/>
      </linearGradient>
      <linearGradient id="middleFill" x1="0" y1="0" x2="1" y2="0">
        <stop offset="0" stop-color="#ffffff"/>
        <stop offset="1" stop-color="#e6e7ea"/>
      </linearGradient>
      <linearGradient id="spaTones" x1="0" y1="0" x2="1" y2="1">
        <stop offset="0" stop-color="#f4e3d6"/>
        <stop offset="1" stop-color="#e7b99e"/>
      </linearGradient>
      <linearGradient id="portraitTones" x1="0" y1="0" x2="0" y2="1">
        <stop offset="0" stop-color="#a9cfe8"/>
        <stop offset="0.45" stop-color="#f0d2bd"/>
        <stop offset="1" stop-color="#e6b597"/>
      </linearGradient>
      <linearGradient id="chamberTones" x1="0" y1="0" x2="1" y2="1">
        <stop offset="0" stop-color="#f3f1ee"/>
        <stop offset="0.6" stop-color="#dcd8d4"/>
        <stop offset="1" stop-color="#b9aba2"/>
      </linearGradient>
      <linearGradient id="darkFill" x1="0" y1="0" x2="1" y2="0">
        <stop offset="0" stop-color="#141517"/>
        <stop offset="0.55" stop-color="#26282b"/>
        <stop offset="1" stop-color="#4a4c50"/>
      </linearGradient>
    </defs>

    <!-- middle panel base -->
    <rect class="panel-bg" x="381" y="0" width="354" height="783" fill="url(#middleFill)"/>

    <!-- left panel blue sweep, kept below the bullet list -->
    <path d="M0,126 C10,320 150,338 381,338" fill="none" stroke="var(--periwinkle)" stroke-width="9"/>
    <path d="M0,150 C12,335 155,352 381,352 L381,783 L0,783 Z" fill="url(#blueFill)"/>

    <!-- spa photo circles -->
    <circle cx="107" cy="387" r="80" fill="#ffffff"/>
    <circle cx="107" cy="387" r="74" fill="url(#spaTones)" role="img" aria-label="Photo of a woman relaxing during a spa massage"/>
    <circle cx="267" cy="392" r="83" fill="#ffffff" stroke="var(--brand-blue)" stroke-width="2"/>
    <circle cx="267" cy="392" r="77" fill="url(#spaTones)" role="img" aria-label="Photo of a woman resting on a towel at the spa"/>

    <!-- middle panel portrait -->
    <path d="M381,455 C480,478 610,452 740,388 L740,783 L381,783 Z" fill="url(#portraitTones)" role="img" aria-label="Portrait photo of a smiling woman holding a frangipani flower"/>
    <path d="M381,435 C480,462 610,440 740,378" fill="none" stroke="var(--periwinkle)" stroke-width="7"/>
    <path d="M381,446 C480,472 610,450 740,386" fill="none" stroke="#ffffff" stroke-width="9"/>

    <!-- right panel photo -->
    <rect x="735" y="0" width="365" height="370" fill="url(#chamberTones)" role="img" aria-label="Photo of a woman inside a whole body cryotherapy chamber"/>

    <!-- dark cover area -->
    <path d="M596,402 C700,325 860,275 1100,258" fill="none" stroke="var(--periwinkle)" stroke-width="9"/>
    <path d="M599,408 C705,335 862,285 1100,268 L1100,722 L599,722 Z" fill="url(#darkFill)"/>
    <rect x="596" y="722" width="504" height="61" fill="var(--footer-grey)"/>
  </svg>

  <!-- left panel -->
  <section class="block intro">
    <h2 class="section-title">What is Whole Body Cryotherapy?</h2>
    <p class="body-copy">Lorem Ipsum is simply dummy text of the printing and typesetting industry. Lorem Ipsum has been the industry's standard dummy text ever since the 1500s, when an unknown printer took a galley of type and scrambled it to make a type specimen book.</p>
  </section>
  <ul class="block benefit-list">
    <li>It has survived not only five centuries, but also the leap into electronic</li>
    <li>Typesetting, remaining essentially unchanged. It was popularised in the</li>
    <li>Typeplate sheets containing Lorem Ipsum passages, and more recently</li>
    <li>Quillset PageForge including versions of Lorem Ipsum.</li>
  </ul>
  <section class="block difference">
    <h2 class="section-title section-title--light">What makes FrostHaven different?</h2>
    <p class="body-copy body-copy--light">Lorem Ipsum is simply dummy text of the printing and typesetting industry. Lorem Ipsum has been the industry's standard dummy text ever since the 1500s, when an unknown printer took a galley of type and scrambled it to make a type specimen book.</p>
    <p class="body-copy body-copy--light">Contrary to popular belief, Lorem Ipsum is not simply random text. It has roots in a piece of classical Latin literature from 45 BC, making it over 2000 years old. Edmund Varlowe, a Latin professor at Ashcombe College in Virginia, looked up one of the more obscure Latin words, consectetur, looked up one of the more obscure Latin words, consectetur,</p>
  </section>

  <!-- middle panel -->
  <section class="block contact">
    <span class="brand-mark"></span>
    <p class="brand-name">FrostHaven</p>
    <address class="address">FrostHaven<br>Lindenmark, 482 W. 19th Street<br>New York, NY 10388</address>
    <p class="contact-line">
      <svg viewBox="0 0 16 16" aria-hidden="true"><path d="M3.5 1.5l2.5 0 1 3.5-1.7 1.2a8 8 0 0 0 4.5 4.5L11 9l3.5 1v2.5c0 1-1 2-2 2C6.6 14.5 1.5 9.4 1.5 3.5c0-1 1-2 2-2z" fill="var(--deep-blue)"/></svg>
      (855) 614-3098
    </p>
    <p class="contact-line contact-line--small">
      <svg viewBox="0 0 16 16" aria-hidden="true"><rect x="1" y="3" width="14" height="10" fill="var(--deep-blue)"/><path d="M1 3.5l7 5 7-5" fill="none" stroke="#fff" stroke-width="1.3"/></svg>
      frosthavenspa@mailbox-example.com
    </p>
    <p class="contact-line contact-line--small">
      <svg viewBox="0 0 16 16" aria-hidden="true"><circle cx="8" cy="8" r="6.5" fill="none" stroke="var(--deep-blue)" stroke-width="1.6"/><path d="M1.5 8h13M8 1.5c-3 3.5-3 9.5 0 13M8 1.5c3 3.5 3 9.5 0 13" fill="none" stroke="var(--deep-blue)" stroke-width="1.2"/></svg>
      www.frosthavenspa-example.com
    </p>
  </section>

  <!-- right panel -->
  <section class="block cover">
    <span class="cover-mark"></span>
    <p class="cover-name">FrostHaven</p>
    <p class="headline-top">FREEZE INTO</p>
    <h1 class="headline-main">FITNESS</h1>
    <p class="tagline">Wholebody Cryotherapy<br>is coming to NYC</p>
    <p class="cover-url">www.frosthavenspa-example.com</p>
  </section>
</main>
</body>
</html>
```